Business Card Design Project

Use our current logo. Clean design.

Industry/Entity Type

Business

Requirements
Must have
• Marisela DUCRANTE
M. Law
Managing Partner

Velotrana AG
Brunnmattweg 274
CH-3097 Liebefeld

M. +41 79 418 26 97
T. +41 31 742 19 04
F. +41 31 742 19 38

m.ducrante@velotrana.example
www.velotrana.example

```html
<!DOCTYPE html>
<html lang="en">
<head>
<meta charset="utf-8">
<title>Velotrana AG – Business Card</title>
<link rel="stylesheet" href="https://fonts.googleapis.com/css2?family=Source+Sans+3:wght@400&family=Tinos:ital@1&display=swap">
<style>
  :root {
    --brand-blue: #1272b9;
    --brand-black: #000000;
    --paper-white: #ffffff;
    --backdrop: #eeeeec;
    --sans: "Source Sans 3", "Myriad Pro", Arial, sans-serif;
    --serif-italic: "Tinos", "Times New Roman", serif;
  }
  * { margin: 0; padding: 0; box-sizing: border-box; }
  html, body {
    width: 1200px; height: 1200px; overflow: hidden;
    background: var(--backdrop);
  }
  .sheet {
    position: relative; width: 1200px; height: 1200px;
  }
  .card {
    position: absolute; left: 200px; width: 800px; height: 500px;
    border-radius: 34px; overflow: hidden;
    box-shadow: 0 6px 18px rgba(0,0,0,.18);
    color: var(--paper-white);
  }
  .card--front { top: 70px; background: var(--brand-blue); }
  .card--back  { top: 630px; background: var(--brand-black); }
  .card__shapes { position: absolute; inset: 0; width: 100%; height: 100%; }

  .wordmark {
    position: absolute; font-family: var(--sans); font-weight: 400;
    color: var(--paper-white); letter-spacing: 2px;
    display: flex; align-items: center; gap: 14px; white-space: nowrap;
  }
  .wordmark__square { background: var(--paper-white); display: block; }
  .card--front .wordmark { left: 48px; top: 210px; font-size: 54px; }
  .card--front .wordmark__square { width: 30px; height: 30px; }
  .card--back .wordmark { right: 70px; top: 60px; font-size: 34px; }
  .card--back .wordmark__square { width: 18px; height: 18px; }

  .holder { position: absolute; left: 448px; top: 118px; font-family: var(--sans); }
  .holder__name { font-size: 34px; line-height: 1.1; white-space: nowrap; }
  .holder__degree { font-size: 24px; margin: 10px 0 0 30px; }
  .holder__role { font-size: 24px; margin: 6px 0 0 58px; white-space: nowrap; }

  .back-text { position: absolute; font-family: var(--serif-italic); font-style: italic; font-size: 32px; line-height: 1.12; white-space: nowrap; }
  .address { left: 44px; top: 178px; }
  .address span { display: block; }
  .address span:nth-child(2) { margin-left: -8px; }
  .address span:nth-child(3) { margin-left: -12px; }
  .phones { left: 390px; top: 232px; text-align: right; }
  .phones span { display: block; }
  .phones span:nth-child(2) { margin-right: 26px; }
  .phones span:nth-child(3) { margin-right: 34px; }
  .online { left: 140px; top: 362px; }
  .online span { display: block; }
</style>
</head>
<body>
<main class="sheet">

  <section class="card card--front" aria-label="Card front">
    <svg class="card__shapes" viewBox="0 0 800 500" aria-hidden="true">
      <path d="M0,0 H300 C400,0 350,130 440,230 C520,320 560,400 500,500 H0 Z" fill="var(--paper-white)"/>
      <path d="M0,0 H280 C380,0 330,130 420,230 C500,320 535,400 475,500 H0 Z" fill="var(--brand-black)"/>
    </svg>
    <div class="wordmark"><span class="wordmark__square"></span>VELOTRANA</div>
    <div class="holder">
      <p class="holder__name">Marisela DUCRANTE</p>
      <p class="holder__degree">M. Law</p>
      <p class="holder__role">Managing Partner</p>
    </div>
  </section>

  <section class="card card--back" aria-label="Card back">
    <svg class="card__shapes" viewBox="0 0 800 500" aria-hidden="true">
      <path d="M0,0 H800 V150 C720,175 640,210 560,175 C440,125 330,40 210,50 C120,58 60,100 0,130 Z" fill="var(--paper-white)"/>
      <path d="M0,0 H800 V136 C720,160 640,192 560,158 C440,108 330,26 210,36 C120,44 60,86 0,116 Z" fill="var(--brand-blue)"/>
    </svg>
    <div class="wordmark"><span class="wordmark__square"></span>VELOTRANA</div>
    <p class="back-text address">
      <span>Velotrana AG</span>
      <span>Brunnmattweg 274</span>
      <span>CH-3097 Liebefeld</span>
    </p>
    <p class="back-text phones">
      <span>M. +41 79 418 26 97</span>
      <span>T. +41 31 742 19 04</span>
      <span>F. +41 31 742 19 38</span>
    </p>
    <p class="back-text online">
      <span>m.ducrante@velotrana.example</span>
      <span>www.velotrana.example</span>
    </p>
  </section>

</main>
</body>
</html>
```